Brambeck Carpets Ltd

I'm looking for a modern looking business card with a logo that's relates to the business, maybe a sheep etc. I will need my name and phone numbers to be included

Industry/Entity Type

Business

Contact Information for Business Card

Neil Hartigan, Director
Phone numbers mobile 07934 206518 and office 0151 763 5042
Carpets and flooring supplied and fitted

```html
<!DOCTYPE html>
<html lang="en">
<head>
<meta charset="utf-8">
<title>Brambeck Carpets Ltd – Business Card</title>
<link rel="stylesheet" href="https://fonts.googleapis.com/css2?family=Jost:wght@300;400;600&display=swap">
<style>
  :root {
    --ink: #1a1f22;
    --ink-soft: #22282b;
    --paper: #ffffff;
  }
  * { margin: 0; padding: 0; box-sizing: border-box; }
  html, body {
    width: 858px;
    height: 1200px;
    overflow: hidden;
    background: var(--ink);
  }
  .card {
    position: relative;
    width: 858px;
    height: 1200px;
    background: var(--ink);
    color: var(--paper);
    font-family: "Jost", "Futura", sans-serif;
  }
  .brand {
    position: absolute;
    top: 0;
    left: 0;
    width: 100%;
    height: 537px;
    display: flex;
    flex-direction: column;
    align-items: center;
  }
  .brand-mark {
    position: absolute;
    top: 170px;
    left: 50%;
    width: 72px;
    height: 72px;
    margin-left: -36px;
    border-radius: 50%;
    background: var(--paper);
  }
  .brand-name {
    position: absolute;
    top: 286px;
    width: 100%;
    text-align: center;
    font-weight: 600;
    font-size: 37px;
    letter-spacing: 0.5px;
  }
  .divider-band {
    position: absolute;
    top: 537px;
    left: 0;
    width: 100%;
    height: 126px;
    background: var(--paper);
  }
  .contact {
    position: absolute;
    top: 768px;
    left: 0;
    width: 100%;
    display: flex;
    flex-direction: column;
    align-items: center;
  }
  .person {
    border: 3px solid var(--paper);
    height: 54px;
    padding: 0 20px;
    display: flex;
    align-items: center;
    font-size: 25px;
    font-weight: 400;
    margin-left: -36px;
  }
  .person .role { font-weight: 300; margin-left: 8px; }
  .phones {
    margin-top: 50px;
    list-style: none;
    font-size: 27px;
    text-align: left;
    margin-left: -6px;
  }
  .phones li { line-height: 58px; }
  .phones .label { font-weight: 400; }
  .phones .number { font-weight: 300; letter-spacing: 1px; }
  .tagline-band {
    position: absolute;
    top: 1054px;
    left: 0;
    width: 100%;
    height: 96px;
    background: var(--ink-soft);
    display: flex;
    align-items: center;
    justify-content: center;
    font-size: 25px;
    font-weight: 300;
    padding-right: 20px;
  }
</style>
</head>
<body>
  <main class="card">
    <header class="brand">
      <div class="brand-mark" aria-hidden="true"></div>
      <h1 class="brand-name">Brambeck Carpets Ltd</h1>
    </header>

    <div class="divider-band"></div>

    <section class="contact">
      <p class="person">Neil Hartigan,<span class="role">Director</span></p>
      <ul class="phones">
        <li><span class="label">Mobile:</span> <span class="number">07934 206518</span></li>
        <li><span class="label">Office:</span> <span class="number">0151 763 5042</span></li>
      </ul>
    </section>

    <footer class="tagline-band">Carpets and flooring supplied and fitted</footer>
  </main>
</body>
</html>
```